all sorted property services

Target Market(s)

General letter head for emails and letter quotes ect

Colors
0054AA
0677BA
7BADD7
CADEEF
E8F1F8
0094D4
00A9DD
6FCCEA
C7EBF8
E9F6FB

Requirements
Must have
• logo phone email website names
Nice to have
• what we do (from the website)

```html
<!DOCTYPE html>
<html lang="en">
<head>
<meta charset="utf-8">
<title>All Sorted Property Services – Letterhead</title>
<link href="https://fonts.googleapis.com/css2?family=Lato:wght@400;700&family=Montserrat:wght@400&display=swap" rel="stylesheet">
<style>
  :root {
    --brand-deep: #0054AA;
    --brand-mid: #0677BA;
    --brand-bright: #0094D4;
    --rule: #1a7fcf;
    --ink: #1b1b1b;
    --ink-soft: #2e2e2e;
    --paper: #ffffff;
    --backdrop: #e6e8eb;
    --sign-tone: #eef1f6;
  }
  * { margin: 0; padding: 0; box-sizing: border-box; }
  html, body { width: 1200px; height: 1141px; overflow: hidden; background: var(--backdrop); }
  .letterhead {
    position: absolute; left: 211px; top: 20px;
    width: 778px; height: 1100px;
    background: var(--paper);
    box-shadow: 0 2px 10px rgba(0,0,0,.12);
    font-family: "Lato", sans-serif;
    color: var(--ink);
  }
  .contact {
    position: absolute; left: 40px; top: 47px;
    font-family: "Montserrat", sans-serif;
    font-size: 13.5px; line-height: 18.5px; color: var(--ink-soft);
  }
  .contact .address { margin-bottom: 6px; }
  .contact .item { display: flex; align-items: center; gap: 5px; }
  .contact svg { width: 11px; height: 11px; fill: var(--brand-mid); flex: none; }
  .brand {
    position: absolute; right: 38px; top: 92px;
    display: flex; align-items: center; gap: 8px;
  }
  .brand-dot { width: 14px; height: 14px; border-radius: 50%; background: var(--brand-deep); }
  .brand-name {
    font-family: "Lato", sans-serif; font-weight: 700;
    font-size: 17px; color: var(--brand-deep); letter-spacing: .3px;
  }
  .header-rule {
    position: absolute; left: 37px; right: 35px; top: 191px;
    height: 2px; background: var(--rule);
  }
  .letter {
    position: absolute; left: 39px; top: 276px; width: 702px;
    font-size: 15.4px; line-height: 18.5px;
  }
  .date { margin-bottom: 20px; }
  .recipient { margin-bottom: 18px; }
  .company { margin-bottom: 22px; }
  .salutation { font-weight: 700; font-size: 19px; line-height: 22px; margin-bottom: 18px; }
  .body p { text-align: justify; line-height: 17.4px; margin-bottom: 17px; }
  .closing { margin-top: 38px; }
  .signature {
    position: absolute; left: 39px; top: 1000px;
    width: 170px; height: 40px; background: var(--sign-tone); border-radius: 4px;
  }
</style>
</head>
<body>
  <main class="letterhead">
    <header>
      <address class="contact" style="font-style:normal">
        <div class="address">Your address, City<br>State, Zip 1234</div>
        <div class="item">
          <svg viewBox="0 0 24 24"><path d="M6.6 10.8a15.1 15.1 0 0 0 6.6 6.6l2.2-2.2c.3-.3.7-.4 1-.2 1.1.4 2.3.6 3.6.6.6 0 1 .4 1 1V20c0 .6-.4 1-1 1A17 17 0 0 1 3 4c0-.6.4-1 1-1h3.5c.6 0 1 .4 1 1 0 1.3.2 2.5.6 3.6.1.3 0 .7-.2 1z"/></svg>
          <span>123 456 789</span>
        </div>
        <div class="item">
          <svg viewBox="0 0 24 24"><path d="M2 5h20v14H2z M4 7l8 6 8-6" stroke="#fff" stroke-width="1.5"/></svg>
          <span>info@allsortedmail.com</span>
        </div>
        <div class="item">
          <svg viewBox="0 0 24 24"><circle cx="12" cy="12" r="10"/></svg>
          <span>www.allsortedsite.com</span>
        </div>
      </address>
      <div class="brand">
        <span class="brand-dot"></span>
        <span class="brand-name">ALL SORTED PROPERTY SERVICES</span>
      </div>
      <div class="header-rule"></div>
    </header>

    <section class="letter">
      <p class="date">January-03-2020</p>
      <p class="recipient">Mr, Peter Hale<br>President</p>
      <p class="company">Harbor Line Corporation<br>123 Street Name, Suite# 10<br>City, State, 120023</p>
      <p class="salutation">Dear Mr, Peter</p>
      <div class="body">
        <p>Lorem ipsum dolor sit amet, consectetur adipiscing elit, sed do eiusmod tempor incididunt ut labore et dolore magna aliqua. Ut enim ad minim veniam, quis nostrud exercitation ullamco laboris nisi ut aliquip ex ea commodo consequat. Duis aute irure dolor in reprehenderit in voluptate velit esse cillum dolore eu fugiat nulla pariatur.</p>
        <p>Lorem ipsum dolor sit amet, consectetur adipiscing elit, sed do eiusmod tempor incididunt ut labore et dolore magna aliqua. Ut enim ad minim veniam, quis nostrud exercitation ullamco laboris nisi ut aliquip ex ea commodo consequat. Duis aute irure dolor in reprehenderit in voluptate velit esse cillum dolore eu fugiat nulla pariatur.</p>
        <p>Lorem ipsum dolor sit amet, consectetur adipiscing elit, sed do eiusmod tempor incididunt ut labore et dolore magna aliqua. Ut enim ad minim veniam, quis nostrud exercitation ullamco laboris nisi ut aliquip ex ea commodo consequat.</p>
        <p>Excepteur sint occaecat cupidatat non proident, sunt in culpa qui officia deserunt mollit anim id est laborum. re et dolore magnam aliquam quaerat voluptatem.</p>
      </div>
      <p class="closing">Regards</p>
    </section>

    <div class="signature" role="img" aria-label="Handwritten signature of Laura Finch"></div>
  </main>
</body>
</html>
```